Gaming Headset Packaging Design

We would like a gaming window box style packaging design for our gaming headset.

We want to use the packaging for 2-3 of our gaming headphone series and hence we would not like to put any product pictures on the packaging.

Size: (enclosed die-cut drawing) please feel free to modify the shape of the window
Material: E Flute Paper box
Type: Window Box style
Design features we prefer: gaming, playful, creative, trendy, High tech.
Requirement: AI file is preferred

Enclosed are a detailed description along with competitor designs and existing die-cut drawing (AI format) for your reference.

Any further questions, please feel free to ask.

```html
<!DOCTYPE html>
<html lang="en">
<head>
<meta charset="UTF-8">
<title>Pro Gaming Headset 7.1 – Window Box Dieline</title>
<link rel="stylesheet" href="https://fonts.googleapis.com/css2?family=Orbitron:wght@700;900&family=Montserrat:wght@400;600;700&display=swap">
<style>
  :root{
    --red:#ec1c24;
    --black:#0b0b0b;
    --white:#ffffff;
    --paper:#ffffff;
    --dark-red:#a5161b;
    --muted:#cfcfcf;
  }
  html,body{margin:0;padding:0;overflow:hidden;background:var(--paper);}
  .canvas{width:1200px;height:1200px;overflow:hidden;background:var(--paper);}
  .dieline{display:block;width:1200px;height:1200px;}
  .panel-red{fill:var(--red);}
  .panel-black{fill:var(--black);}
  .window{fill:var(--white);stroke:var(--red);stroke-width:3;}
  .title{font-family:"Orbitron",sans-serif;font-weight:900;}
  .title-white{fill:var(--white);}
  .title-black{fill:var(--black);}
  .title-red{fill:var(--red);}
  .brand{font-family:"Orbitron",sans-serif;font-weight:700;font-size:9px;fill:var(--white);}
  .brand-accent{fill:var(--red);}
  .corner{fill:none;stroke:var(--muted);stroke-width:1;}
  .spec-head{font-family:"Montserrat",sans-serif;font-weight:700;font-size:5.6px;fill:var(--white);}
  .spec{font-family:"Montserrat",sans-serif;font-weight:400;font-size:5px;fill:var(--white);}
  .label-tag{fill:var(--red);}
  .label{font-family:"Montserrat",sans-serif;font-weight:700;font-size:6px;fill:var(--white);}
  .feature{fill:var(--dark-red);stroke:var(--red);stroke-width:0.8;}
  .feature-text{font-family:"Montserrat",sans-serif;font-weight:600;font-size:3.4px;fill:var(--white);text-anchor:middle;}
  .cert{fill:none;stroke:var(--white);stroke-width:1.6;}
  .cert-solid{fill:var(--white);}
</style>
</head>
<body>
<div class="canvas">
<svg class="dieline" viewBox="215 547 1100 1100" xmlns="http://www.w3.org/2000/svg">
  <defs>
    <radialGradient id="headsetGlowDark" cx="50%" cy="55%" r="55%">
      <stop offset="0" stop-color="#3a0b0d"/>
      <stop offset="1" stop-color="#0b0b0b" stop-opacity="0"/>
    </radialGradient>
    <radialGradient id="headsetGlowRed" cx="60%" cy="45%" r="55%">
      <stop offset="0" stop-color="#c8141b"/>
      <stop offset="1" stop-color="#ec1c24" stop-opacity="0"/>
    </radialGradient>
  </defs>

  <!-- Left side panel with flaps -->
  <g class="side-left">
    <polygon class="panel-red" points="247,947 277,850 420,850 423,947"/>
    <rect class="panel-red" x="247" y="947" width="176" height="398"/>
    <polygon class="panel-red" points="247,1345 423,1345 423,1395 330,1425 330,1465 247,1465"/>
    <rect x="250" y="1000" width="173" height="300" fill="url(#headsetGlowRed)" role="img" aria-label="Faint line illustration of a gaming headset"/>
    <text class="title title-white" font-size="27" textLength="305" lengthAdjust="spacingAndGlyphs" transform="translate(308,1312) rotate(-90)">PRO GAMING</text>
    <text class="title title-black" font-size="42" textLength="335" lengthAdjust="spacingAndGlyphs" transform="translate(350,1312) rotate(-90)">HEADSET 7.1</text>
  </g>

  <!-- Top lid flap -->
  <g class="lid">
    <path class="panel-red" d="M425,947 L425,748 Q425,732 441,732 L733,732 Q749,732 749,748 L749,947 Z"/>
    <rect x="625" y="740" width="124" height="200" fill="url(#headsetGlowRed)" role="img" aria-label="Faint line illustration of a gaming headset"/>
    <g transform="rotate(180 588 862)">
      <text class="title title-white" font-size="12" x="508" y="857" textLength="160" lengthAdjust="spacingAndGlyphs">PRO GAMING</text>
      <text class="title title-black" font-size="16" x="508" y="875" textLength="160" lengthAdjust="spacingAndGlyphs">HEADSET 7.1</text>
    </g>
  </g>

  <!-- Right side top flap and back tab -->
  <polygon class="panel-red" points="755,947 755,850 875,850 905,947"/>
  <path class="panel-red" d="M1058,947 L1058,890 Q1058,883 1065,883 L1113,883 Q1120,883 1120,890 L1120,947 Z"/>

  <!-- Main black body: front, side, back -->
  <rect class="panel-black" x="423" y="947" width="832" height="398"/>

  <!-- Glue flap -->
  <polygon class="panel-red" points="1255,947 1285,962 1285,1330 1255,1345"/>

  <!-- Bottom flaps -->
  <polygon class="panel-black" points="423,1345 750,1345 750,1465 672,1465 672,1430 520,1430 520,1465 423,1465"/>
  <polygon class="panel-red" points="750,1345 840,1345 840,1465 790,1465 790,1420 750,1400"/>
  <polygon class="panel-black" points="840,1345 1252,1345 1172,1440 1172,1465 930,1465 930,1430 880,1430 880,1465 840,1465"/>

  <!-- Headset illustration on front -->
  <rect x="360" y="1000" width="200" height="290" fill="url(#headsetGlowDark)" role="img" aria-label="Faint line illustration of a gaming headset"/>

  <!-- Window -->
  <polygon class="window" points="622,1040 680,993 820,993 826,999 918,999 922,990 998,990 1023,1013 1023,1268 995,1296 725,1296 680,1268 622,1268"/>

  <!-- Front title -->
  <g class="front-title">
    <text class="title title-white" font-size="13" textLength="108" lengthAdjust="spacingAndGlyphs" transform="translate(444,1068) rotate(-90)">PRO GAMING</text>
    <text class="title title-red" font-size="16" textLength="85" lengthAdjust="spacingAndGlyphs" transform="translate(462,1068) rotate(-90)">HEADSET</text>
    <text class="title title-red" font-size="24" x="466" y="983" textLength="40" lengthAdjust="spacingAndGlyphs">7.1</text>
  </g>

  <!-- Company name -->
  <g class="brand-block">
    <path class="corner" d="M555,970 V964 H561 M629,964 H635 V970 M635,1006 V1012 H629 M561,1012 H555 V1006"/>
    <text class="brand" x="595" y="985" text-anchor="middle">COMPANY</text>
    <text class="brand brand-accent" x="595" y="996" text-anchor="middle">NAME</text>
  </g>

  <!-- Feature badges -->
  <g class="features">
    <circle class="feature" cx="447" cy="1312" r="18"/>
    <text class="feature-text" x="447" y="1308">Virtual 7.1</text><text class="feature-text" x="447" y="1313">Surround</text><text class="feature-text" x="447" y="1318">Sound</text>
    <circle class="feature" cx="486" cy="1312" r="18"/>
    <text class="feature-text" x="486" y="1308">Dual Drivers</text><text class="feature-text" x="486" y="1313">on Each Ear</text><text class="feature-text" x="486" y="1318">for Accuracy</text>
    <circle class="feature" cx="525" cy="1312" r="18"/>
    <text class="feature-text" x="525" y="1310">3D Sound</text><text class="feature-text" x="525" y="1315">Vibration</text>
    <circle class="feature" cx="564" cy="1312" r="18"/>
    <text class="feature-text" x="564" y="1308">Bendable</text><text class="feature-text" x="564" y="1313">Stainless Steel</text><text class="feature-text" x="564" y="1318">Headband</text>
    <circle class="feature" cx="603" cy="1312" r="18"/>
    <text class="feature-text" x="603" y="1310">Soft &amp; Soothing</text><text class="feature-text" x="603" y="1315">Earpads</text>
  </g>

  <!-- Back panel specifications -->
  <g class="specs">
    <path class="label-tag" d="M1030,962 L1108,960 L1112,972 L1034,974 Z"/>
    <text class="label" x="1043" y="971">Specification</text>
    <line x1="1036" y1="976" x2="1245" y2="976" stroke="#ec1c24" stroke-width="0.8"/>

    <text class="spec-head" x="1037" y="988">Headphone Specification</text>
    <text class="spec" x="1037" y="1001">Speaker Diameter: Ø40mm</text>
    <text class="spec" x="1037" y="1012">Impedance: 32Ω ± 15</text>
    <text class="spec" x="1037" y="1023">Sensitivity S.P.L: 113dB ± 3dB</text>
    <text class="spec" x="1037" y="1034">Rated Power: 20mW</text>
    <text class="spec" x="1037" y="1045">Aggregate capability: 30mW</text>
    <text class="spec" x="1037" y="1056">Frequency Response: 20-20kHz</text>
    <text class="spec" x="1037" y="1067">Plug Type: 3.5mm Stereo</text>

    <text class="spec-head" x="1145" y="988">Microphone Specification</text>
    <text class="spec" x="1145" y="1001">Microphone Unit: Ø6 x 5mm</text>
    <text class="spec" x="1145" y="1012">Sensitivity S.P.L 34dB ± 3dB</text>
    <text class="spec" x="1145" y="1023">Impedance: &lt;2.2k</text>
    <text class="spec" x="1145" y="1034">Frequency Response: 30-16kHz</text>
    <text class="spec" x="1145" y="1045">Standard Operating Voltage: 4.5V</text>
    <text class="spec" x="1145" y="1056">S/N Ratio: ≥ 60dB</text>
    <text class="spec" x="1145" y="1067">Plug Type: 3.5mm Stereo</text>

    <path class="label-tag" d="M1032,1076 L1074,1075 L1076,1085 L1034,1086 Z"/>
    <text class="label" x="1038" y="1083" font-size="5">Warning:</text>
    <text class="spec" x="1034" y="1096">Adjust headphone's sound to a proper volume. Loud sound may damage</text>
    <text class="spec" x="1034" y="1107">your ears. For traffic safety never use the headset while driving.</text>

    <path class="label-tag" d="M1032,1117 L1070,1116 L1072,1126 L1034,1127 Z"/>
    <text class="label" x="1038" y="1124" font-size="5">Caution:</text>
    <text class="spec" x="1034" y="1138">If the user attempts to inspect or modify the product in any way we</text>
    <text class="spec" x="1034" y="1148">don't guarantee the performance of the product. Specifications and</text>
    <text class="spec" x="1034" y="1158">design are subject to possible modification notice due to improvements.</text>

    <path class="corner" d="M1036,1174 V1168 H1042 M1237,1168 H1243 V1174 M1243,1231 V1237 H1237 M1042,1237 H1036 V1231"/>

    <text class="spec" x="1034" y="1250">© 2019 Lorem ipsum dolor sit amet,</text>
    <text class="spec" x="1034" y="1261">consectetur adipiscing elit. Curabitur dapibus vitae mauris consectetur</text>
    <text class="spec" x="1034" y="1271">fermentum. Pellentesque eleifend vel orci non tristique. Donec a orci</text>
    <text class="spec" x="1034" y="1281">luctus, bibendum leo a, hendrerit nunc. Proin tristique dolor ut.</text>
  </g>

  <!-- Certification badges (plain shapes) -->
  <g class="certifications" aria-label="Certification marks">
    <rect class="cert-solid" x="1035" y="1308" width="22" height="16" rx="2"/>
    <circle class="cert" cx="1077" cy="1316" r="8"/>
    <polygon class="cert" points="1120,1306 1131,1325 1109,1325"/>
    <circle class="cert" cx="1153" cy="1316" r="8"/>
    <rect class="cert" x="1173" y="1308" width="14" height="16"/>
    <polygon class="cert" points="1207,1307 1215,1323 1199,1323"/>
    <circle class="cert-solid" cx="1233" cy="1316" r="9"/>
  </g>
</svg>
</div>
</body>
</html>
```